Volt menders . Energy efficiency improvement for residential and commercial/industrial

Logo needed for “ volt menders .com “ website. Conduct energy audits and provide consulting about efficiency improvements . I will provide content for pages about 10 pages . Get customer serway and store information .
Some pages will be copied from Lumacrestbyx.com

```html
<!DOCTYPE html>
<html lang="en">
<head>
<meta charset="utf-8">
<title>Volt Menders</title>
<link href="https://fonts.googleapis.com/css2?family=Montserrat:wght@800&family=Poppins:wght@300;400;500;600&display=swap" rel="stylesheet">
<style>
:root{
  --blue:#1238e0;
  --blue-text:#1534d6;
  --ink:#222;
  --body:#444;
  --dark:#0e0e10;
  --white:#fff;
  --line:#bbb;
}
*{margin:0;padding:0;box-sizing:border-box}
html,body{width:1200px;height:2749px;overflow:hidden;background:var(--white)}
body{position:relative;font-family:"Poppins",sans-serif;color:var(--ink)}
.btn{position:absolute;display:flex;align-items:center;justify-content:center;color:var(--white);font-size:15px;font-weight:400;background:var(--blue)}
.btn.dark{background:#111}

/* header */
.site-header{position:absolute;left:0;top:0;width:1200px;height:55px;background:var(--white)}
.brand{position:absolute;left:144px;top:15px;display:flex;align-items:center;gap:8px}
.brand-dot{width:30px;height:30px;border-radius:50%;background:var(--blue)}
.brand-name{font-weight:600;font-size:16px;color:var(--blue)}
.main-nav{position:absolute;right:144px;top:24px;display:flex;gap:19px;font-size:13px;color:#333}

/* hero */
.hero{position:absolute;left:0;top:55px;width:1200px;height:562px;
  background:radial-gradient(ellipse at 58% 45%,#6a4fd6 0%,#2a3fb8 25%,#14236d 55%,#0a1238 100%)}
.hero h1{position:absolute;left:141px;top:178px;font-family:"Montserrat",sans-serif;font-weight:800;color:var(--white);line-height:1.15}
.hero .l1{display:block;font-size:44px}
.hero .l2{display:block;font-size:45px;letter-spacing:6px}
.hero p{position:absolute;left:142px;top:292px;font-size:20px;font-weight:300;color:var(--white)}
.hero .btn{left:145px;top:333px;width:167px;height:42px;font-size:17px;letter-spacing:2px}
.dots{position:absolute;left:1103px;top:205px;display:flex;flex-direction:column;align-items:center;gap:8px}
.dots span{display:flex;align-items:center;justify-content:center;border:2px solid var(--white);border-radius:50%;color:var(--white);font-size:14px;font-weight:500}

/* section headings */
.heading{position:absolute;left:0;width:1200px;text-align:center;font-weight:500;font-size:38px}
.heading.blue{color:var(--blue-text);font-weight:600}

/* services */
.card{position:absolute;top:721px;width:300px;height:387px;border:1px solid #999;background:var(--white)}
.card .pic{height:188px}
.card h3{margin-top:20px;text-align:center;font-size:17px;font-weight:400}
.card p{margin:8px 14px 0;text-align:center;font-size:12px;line-height:18.5px;letter-spacing:-0.15px;color:var(--body);font-weight:300}
.card .btn{left:88px;top:327px;width:123px;height:35px}

/* about band */
.band{position:absolute;left:0;top:1169px;width:1200px;height:241px;
  background:linear-gradient(90deg,#1a2fb0,#2643d8 30%,#3a3bd0 50%,#2643d8 70%,#1a2fb0)}
.band h2{position:absolute;left:0;top:48px;width:1200px;text-align:center;color:var(--white);font-size:38px;font-weight:500}
.panel{position:absolute;left:143px;top:1290px;width:911px;height:340px;background:var(--white)}
.copy{position:absolute;font-size:12.5px;line-height:21px;letter-spacing:-0.1px;color:var(--body);font-weight:300}
.copy p+p{margin-top:21px}
.photo{position:absolute}

/* footer */
.site-footer{position:absolute;left:0;top:2455px;width:1200px;height:294px;background:var(--dark);color:var(--white)}
.f-logo{position:absolute;left:187px;top:52px;width:63px;height:63px;border-radius:50%;background:var(--blue)}
.f-name{position:absolute;left:134px;top:120px;width:171px;text-align:center;font-weight:600;font-size:19px;color:var(--blue)}
.socials{position:absolute;left:156px;top:175px;display:flex;gap:3px}
.socials span{width:30px;height:30px;border:1.5px solid var(--white);border-radius:50%}
.f-title{position:absolute;font-size:15px;font-weight:500}
.contact-row{position:absolute;left:362px;display:flex;gap:16px;font-size:15px;font-weight:600;line-height:28px}
.contact-row svg{flex:none;margin-top:4px}
.divider{position:absolute;left:702px;top:40px;width:1px;height:185px;background:#888}
.links{position:absolute;font-size:12.5px;line-height:24px;list-style:none}
.links.wide{line-height:34px}
.rule{position:absolute;left:143px;top:238px;width:912px;height:1px;background:#888}
.copyright{position:absolute;left:0;top:256px;width:1200px;text-align:center;font-size:13px}
</style>
</head>
<body>

<header class="site-header">
  <div class="brand"><span class="brand-dot"></span><span class="brand-name">Volt Menders</span></div>
  <nav class="main-nav"><span>Home</span><span>New for 2021</span><span>What We Do?</span><span>How Its Works</span><span>About</span><span>Contact Us</span></nav>
</header>

<section class="hero" role="img" aria-label="Night city skyline with glowing blue and violet light streaks rising from the streets">
  <h1><span class="l1">Welcome to</span><span class="l2">VOLTMENDERS.COM</span></h1>
  <p>Energy efficiency improvement for residential and commercial/industrial</p>
  <span class="btn">READ MORE</span>
  <div class="dots"><span style="width:40px;height:40px;font-size:17px">01</span><span style="width:28px;height:28px">02</span><span style="width:28px;height:28px">03</span></div>
</section>

<h2 class="heading" style="top:660px">What We Do</h2>

<article class="card" style="left:144px">
  <div class="pic" role="img" aria-label="Hand holding a glowing light bulb containing a solar field" style="background:radial-gradient(circle at 45% 55%,#8fb6e0 0%,#2a4d86 25%,#0e1a30 70%)"></div>
  <h3>Energy Savings</h3>
  <p>Lorem Ipsum is simply dummy text of the printing and typesetting industry. Lorem Ipsum has been the industry's standard dummy text ever since the 1500s,</p>
  <span class="btn dark">Read More</span>
</article>
<article class="card" style="left:450px">
  <div class="pic" role="img" aria-label="Engineer in a hard hat inspecting rows of solar panels" style="background:linear-gradient(180deg,#b9d2ec 0%,#8fb0d8 35%,#3b5fae 60%,#283f82 100%)"></div>
  <h3>Operating Efficiency</h3>
  <p>Lorem Ipsum is simply dummy text of the printing and typesetting industry. Lorem Ipsum has been the industry's standard dummy text ever since the 1500s,</p>
  <span class="btn">Read More</span>
</article>
<article class="card" style="left:756px">
  <div class="pic" role="img" aria-label="Silhouettes of two workers in hard hats shaking hands by a window" style="background:linear-gradient(90deg,#3a3a3e,#c9c2b8 50%,#3a3a3e)"></div>
  <h3>Reliability &amp; Sustainability</h3>
  <p>Lorem Ipsum is simply dummy text of the printing and typesetting industry. Lorem Ipsum has been the industry's standard dummy text ever since the 1500s,</p>
  <span class="btn dark">Read More</span>
</article>

<section class="band" role="img" aria-label="Blue city skyline with light streaks"><h2>Volt Menders</h2></section>
<div class="panel"></div>
<div class="copy" style="left:166px;top:1317px;width:420px">
  <p>Volt Menders is the Swiss-Army-Knife of real-time equipment monitoring. It can save manufacturers a great deal in terms of energy-cost, machine-reliability, management time and improved maintenance.</p>
  <p>In many utility areas, rebates and incentives are offered for energy-reduction projects, which in most cases would pay for 50-100% of the capital cost of a complete Lumacrest installation.</p>
</div>
<span class="btn" style="left:166px;top:1506px;width:123px;height:35px">More About</span>
<div class="photo" role="img" aria-label="Hand holding a glowing light bulb surrounded by a network of connected points" style="left:597px;top:1323px;width:433px;height:263px;background:radial-gradient(circle at 30% 30%,#f4d7c0 0%,#c99a84 15%,#5d9b94 45%,#c9a27e 100%)"></div>

<h2 class="heading blue" style="top:1643px">Your Company Goals</h2>
<div class="photo" role="img" aria-label="Cupped hands holding a green glass globe over grass" style="left:165px;top:1722px;width:434px;height:263px;background:radial-gradient(circle at 50% 55%,#9fd66a 0%,#3f9a2e 35%,#1d5a1a 100%)"></div>
<div class="copy" style="left:638px;top:1717px;width:420px">
  <p>Do your company goals include reducing waste, increasing operational efficiency, increasing competitive advantage, strengthening brand reputation and enhancing long-term business viability?</p>
  <p>Volt Menders provides the detailed data necessary to analyze and measure progress towards these goals.</p>
</div>
<span class="btn" style="left:638px;top:1904px;width:123px;height:35px">Learn More</span>

<h2 class="heading blue" style="top:2032px">Modern Facility-Management</h2>
<div class="copy" style="left:166px;top:2107px;width:420px">
  <p>Whether you have sustainability goals, efficiency targets, or sub-metering requirements (e.g. ISO 50001), modern operations for facility-management and manufacturing require economically-sound processes to minimize environmental impact while conserving energy and natural resources.</p>
  <p>To help achieve these goals, Lumacrest provides...</p>
</div>
<span class="btn" style="left:166px;top:2296px;width:123px;height:35px">Learn More</span>
<div class="photo" role="img" aria-label="Solar panel field at sunset under an orange and purple sky" style="left:597px;top:2113px;width:433px;height:263px;background:linear-gradient(180deg,#6a6a9a 0%,#d38a4e 40%,#f0b050 48%,#5a4a3a 60%,#2e3a22 100%)"></div>

<footer class="site-footer">
  <div class="f-logo"></div>
  <div class="f-name">Volt Menders</div>
  <div class="socials"><span></span><span></span><span></span><span></span></div>

  <div class="f-title" style="left:362px;top:32px">Contact Us</div>
  <div class="contact-row" style="top:70px">
    <svg width="18" height="18" viewBox="0 0 24 24"><path fill="#fff" d="M6.6 10.8c1.4 2.8 3.8 5.1 6.6 6.6l2.2-2.2c.3-.3.7-.4 1-.2 1.1.4 2.3.6 3.6.6.6 0 1 .4 1 1V20c0 .6-.4 1-1 1C10.6 21 3 13.4 3 4c0-.6.4-1 1-1h3.5c.6 0 1 .4 1 1 0 1.3.2 2.5.6 3.6.1.3 0 .7-.2 1z"/></svg>
    <span>Phone: +555-214-0387</span></div>
  <div class="contact-row" style="top:105px">
    <svg width="18" height="18" viewBox="0 0 24 24"><path fill="#fff" d="M2 5h20v14H2z"/><path d="M2 5l10 8 10-8" fill="none" stroke="#0e0e10" stroke-width="2"/></svg>
    <span>Email:&nbsp; Support@VoltMenders.com</span></div>
  <div class="contact-row" style="top:143px">
    <svg width="18" height="22" viewBox="0 0 24 30"><path fill="#fff" d="M12 0C5.4 0 0 5.4 0 12c0 9 12 18 12 18s12-9 12-18C24 5.4 18.6 0 12 0zm0 17a5 5 0 110-10 5 5 0 010 10z"/></svg>
    <span>218 Larkfield Avenue, Brookhaven City<br>Westmark, 40912.</span></div>

  <div class="divider"></div>
  <div class="f-title" style="left:760px;top:35px">Quick links</div>
  <ul class="links" style="left:760px;top:62px"><li>Home</li><li>New for 2021</li><li>What We Do?</li><li>How Its Works</li><li>About</li><li>Contact Us</li></ul>
  <ul class="links wide" style="left:904px;top:57px"><li>Energy Savings</li><li>Operating Efficiency</li><li>Reliability &amp; Sustainability</li></ul>

  <div class="rule"></div>
  <div class="copyright">VoltMenders.com © 2021 All Rights Reserved.</div>
</footer>

</body>
</html>
```